K.E.L Ventures - Business Card

We need a business card design for a new company based in Malaysia, called K.E.L Ventures Sdn. Bhd. We create, develop & customize database & software/web-based business systems to suit our clients need, mainly in oil&gas industry.

We would like to challenge the creativity of you to design a simple, meaningful, modern, professional & sleek. The design concept may varies but worthy enough for the recipients to proudly keep it in their wallet, and award us with fruitful business opportunities.

B-3-12 Meridan Plaza,
SS21/4, Subang Jaya,
46300 Selangor. Malaysia

http://kelventures-example.com

HAFIZ Roslan | +6012-3817260 | Co-Founder
Di Nazwan | +6012-4092731 | Co-Founder
Abdul Kamil | +6019-5063184 | Managing Director

Target Market(s)

The target market will expand to several other industries such as aviation, communication, automotive, education & hotel.

Industry/Entity Type

Business

Font styles to use
Serif
Sans Serif
Decorative
Script

Requirements
Must have
• plain background yet colourful concept.
Should not have
• something too easy that I can draw myself

```html
<!DOCTYPE html>
<html lang="en">
<head>
<meta charset="utf-8">
<title>K.E.L Ventures – Business Card</title>
<link rel="stylesheet" href="https://fonts.googleapis.com/css2?family=Didact+Gothic&family=Roboto+Condensed:wght@400&display=swap">
<style>
  :root {
    --page-bg: #eeeeec;
    --card-bg: #ffffff;
    --brand-green: #8dc21f;
    --name-green: #2f5a1f;
    --ink-dark: #2e4325;
    --band-ink: #33461c;
    --rule-grey: #b9beb5;
    --accent-orange: #f0961e;
  }
  * { margin: 0; padding: 0; box-sizing: border-box; }
  html, body {
    width: 1200px; height: 820px; overflow: hidden;
    background: var(--page-bg);
  }
  .card {
    position: absolute; left: 40px; top: 66px;
    width: 1120px; height: 688px;
    background: var(--card-bg);
    font-family: "Didact Gothic", sans-serif;
  }
  .brand-name {
    position: absolute; left: 0; right: 0; top: 52px;
    text-align: center;
    font-size: 92px; line-height: 1;
    color: var(--brand-green);
    letter-spacing: 2px;
    white-space: nowrap;
  }
  .team { position: absolute; left: 0; top: 0; width: 1120px; height: 542px; }
  .member-name {
    position: absolute; width: 300px; text-align: center;
    font-size: 35px; line-height: 1; color: var(--name-green);
    white-space: nowrap;
  }
  .member-name::after {
    content: ""; display: block; margin: 6px auto 0;
    width: 210px; height: 1px; background: var(--rule-grey);
  }
  .member-role {
    position: absolute; width: 300px; text-align: center;
    font-family: "Roboto Condensed", sans-serif;
    font-size: 23px; line-height: 1; color: var(--name-green);
    white-space: nowrap;
  }
  .divider {
    position: absolute; left: 549px; top: 222px;
    width: 3px; height: 286px; border-radius: 2px;
    background: var(--accent-orange);
  }
  .phone {
    position: absolute; font-size: 28px; line-height: 1;
    color: var(--ink-dark); letter-spacing: 1.5px;
    white-space: nowrap;
  }
  .contact-band {
    position: absolute; left: 0; top: 542px;
    width: 1120px; height: 120px;
    background: var(--brand-green);
  }
  .icon { position: absolute; }
  .address {
    position: absolute; left: 123px; top: 14px;
    font-size: 25px; line-height: 31px; color: var(--band-ink);
    letter-spacing: 1px; white-space: nowrap;
  }
  .website {
    position: absolute; left: 710px; top: 41px;
    font-size: 25px; line-height: 1; color: var(--band-ink);
    letter-spacing: 0.5px; white-space: nowrap;
  }
</style>
</head>
<body>
  <div class="card">
    <div class="brand-name">K.E.L Ventures</div>

    <div class="team">
      <div class="member-name" style="left:192px; top:228px;">HAFIZ Roslan</div>
      <div class="member-role" style="left:192px; top:273px;">Co-Founder</div>
      <div class="phone" style="left:616px; top:242px;">+6012-3817260</div>

      <div class="member-name" style="left:192px; top:327px;">Di Nazwan</div>
      <div class="member-role" style="left:192px; top:372px;">Co-Founder</div>
      <div class="phone" style="left:629px; top:330px;">+6012-4092731</div>

      <div class="member-name" style="left:192px; top:420px;">Abdul Kamil</div>
      <div class="member-role" style="left:192px; top:466px;">Managing Director</div>
      <div class="phone" style="left:629px; top:442px;">+6019-5063184</div>
    </div>

    <div class="divider"></div>

    <div class="contact-band">
      <svg class="icon home-icon" style="left:38px; top:30px;" width="72" height="46" viewBox="0 0 72 46" aria-hidden="true">
        <polygon points="36,2 70,24 62,24 36,8 10,24 2,24" fill="#ffffff"/>
        <polygon points="14,24 36,11 58,24 58,44 42,44 42,32 30,32 30,44 14,44" fill="#ffffff"/>
      </svg>
      <div class="address">
        B-3-12 Meridan Plaza,<br>
        SS21/4, Subang Jaya,<br>
        46300 Selangor. Malaysia
      </div>

      <svg class="icon web-icon" style="left:626px; top:26px;" width="66" height="52" viewBox="0 0 66 52" aria-hidden="true">
        <rect x="2" y="2" width="62" height="48" rx="3" fill="none" stroke="#ffffff" stroke-width="3"/>
        <circle cx="33" cy="26" r="15" fill="none" stroke="#ffffff" stroke-width="2.5"/>
        <ellipse cx="33" cy="26" rx="6" ry="15" fill="none" stroke="#ffffff" stroke-width="2"/>
        <line x1="18" y1="26" x2="48" y2="26" stroke="#ffffff" stroke-width="2"/>
        <line x1="21" y1="18" x2="45" y2="18" stroke="#ffffff" stroke-width="1.5"/>
        <line x1="21" y1="34" x2="45" y2="34" stroke="#ffffff" stroke-width="1.5"/>
      </svg>
      <div class="website">http://kelventures-example.com</div>
    </div>
  </div>
</body>
</html>
```